Vertice Norte needs the best stationery in the development business

We need a stationary design for a new company based in Porto, Portugal. We are a new property development management company specialized in downtown regeneration projects and adaptive use of old big textile factories.

We just have selected our new logo in a pixelhive competition and now we are searching for the best stationary design. We expect to receive proposals for:

Two sided business cards
A4 main letterhead
A4 simple text papper
A4 and A5 envelops
A4 single folder front page

information for the stationary project

company signature: RaizProjetoFuturo (as in the logo files attached)

Business card information: 
Henrique Moura Salgado MBQS
Managing Director

email: henrique@verticenorte.example.pt
website: www.verticenorte.example.pt

adress: 
R. das Oliveiras, 71 - 2º
4100-218 Porto

office number
+(351) 22 418 76 03
fax number
+(351) 22 418 76 05
mobile
+(351) 913 204 671

Target Market(s)

professional finantial fund managers and big property owners

Industry/Entity Type

Business

Requirements
Must have
• the company logo

Nice to have
• clear simple contemporary design is appreciated

```html
<!DOCTYPE html>
<html lang="pt">
<head>
<meta charset="utf-8">
<title>Vertice Norte – Business Card</title>
<link href="https://fonts.googleapis.com/css2?family=Source+Sans+3:wght@400;600;700&display=swap" rel="stylesheet">
<style>
  :root {
    --brand-blue: #2a63b1;
    --brand-grey: #a7a7a9;
    --paper: #ffffff;
    --stage: #e9ebee;
    --ink-light: #ffffff;
    --icon-grey: #c9ccd3;
  }
  * { box-sizing: border-box; margin: 0; padding: 0; }
  html, body { width: 986px; height: 1200px; overflow: hidden; }
  body {
    background: var(--stage);
    font-family: "Source Sans 3", Arial, sans-serif;
    position: relative;
  }
  .card {
    position: absolute;
    left: 83px;
    width: 820px;
    height: 460px;
    border-radius: 34px;
    overflow: hidden;
    box-shadow: 0 10px 28px rgba(0,0,0,0.18);
  }
  .card--front { top: 110px; background: var(--paper); }
  .card--back { top: 630px; background: var(--brand-blue); }

  .card__waves { position: absolute; inset: 0; }

  .brand {
    position: absolute;
    text-align: center;
    left: 0; right: 0;
  }
  .brand__dot {
    display: block;
    margin: 0 auto 8px;
    border-radius: 50%;
  }
  .brand__name {
    font-weight: 700;
    letter-spacing: -1px;
    line-height: 1;
    white-space: nowrap;
  }
  .card--front .brand { top: 42px; }
  .card--front .brand__dot { width: 38px; height: 38px; background: var(--brand-blue); }
  .card--front .brand__name { font-size: 62px; color: var(--brand-blue); }
  .brand__tagline {
    margin-top: 6px;
    font-size: 22px;
    font-weight: 600;
    color: var(--brand-blue);
    letter-spacing: 0.2px;
  }
  .card--back .brand { top: 168px; }
  .card--back .brand__dot { width: 44px; height: 44px; background: var(--ink-light); }
  .card--back .brand__name { font-size: 64px; color: var(--ink-light); }

  .person {
    position: absolute;
    right: 420px;
    top: 298px;
    text-align: right;
    color: var(--ink-light);
  }
  .person__name { font-size: 21px; font-weight: 700; white-space: nowrap; }
  .person__role { font-size: 17px; margin-top: 1px; }
  .phones { list-style: none; margin-top: 12px; }
  .phones li {
    display: flex; justify-content: flex-end; align-items: center;
    gap: 8px; font-size: 17px; line-height: 25px; white-space: nowrap;
  }
  .icon { width: 18px; height: 18px; flex: none; }

  .divider {
    position: absolute;
    left: 418px; top: 290px;
    width: 2px; height: 130px;
    background: var(--ink-light);
  }

  .contact {
    position: absolute;
    left: 436px; top: 292px;
    color: var(--ink-light);
  }
  .contact__links { list-style: none; }
  .contact__links li {
    display: flex; align-items: center; gap: 8px;
    font-size: 17px; line-height: 26px; white-space: nowrap;
  }
  .contact__address {
    font-style: normal;
    font-size: 17px;
    line-height: 24px;
    margin-top: 34px;
    padding-left: 4px;
  }
</style>
</head>
<body>

<section class="card card--front" aria-label="Business card front">
  <svg class="card__waves" width="820" height="460" viewBox="0 0 820 460" aria-hidden="true">
    <path d="M0,268 Q380,318 820,168 L820,460 L0,460 Z" fill="var(--brand-grey)"/>
    <path d="M0,282 Q390,326 820,186 L820,460 L0,460 Z" fill="var(--brand-blue)"/>
  </svg>

  <div class="brand">
    <span class="brand__dot"></span>
    <div class="brand__name">Vertice Norte</div>
    <div class="brand__tagline">RaizProjetoFuturo</div>
  </div>

  <div class="person">
    <div class="person__name">Henrique Moura Salgado MBQS</div>
    <div class="person__role">Managing Director</div>
    <ul class="phones">
      <li>+(351) 22 418 76 03
        <svg class="icon" viewBox="0 0 18 18" aria-label="Office"><circle cx="9" cy="9" r="9" fill="var(--icon-grey)"/><path d="M5.5,4.5 l2,0 1,3 -1.3,1 a6,6 0 0 0 2.3,2.3 l1,-1.3 3,1 0,2 a1,1 0 0 1 -1,1 A8,8 0 0 1 4.5,5.5 a1,1 0 0 1 1,-1z" fill="var(--brand-blue)"/></svg>
      </li>
      <li>+(351) 22 418 76 05
        <svg class="icon" viewBox="0 0 18 18" aria-label="Fax"><circle cx="9" cy="9" r="9" fill="var(--icon-grey)"/><rect x="5" y="7" width="8" height="6" rx="1" fill="var(--brand-blue)"/><rect x="6.5" y="4" width="5" height="3" fill="var(--brand-blue)"/></svg>
      </li>
      <li>+(351) 913 204 671
        <svg class="icon" viewBox="0 0 18 18" aria-label="Mobile"><circle cx="9" cy="9" r="9" fill="var(--icon-grey)"/><rect x="6" y="3.5" width="6" height="11" rx="1.2" fill="var(--brand-blue)"/><rect x="7" y="5" width="4" height="6" fill="var(--icon-grey)"/></svg>
      </li>
    </ul>
  </div>

  <div class="divider"></div>

  <div class="contact">
    <ul class="contact__links">
      <li>
        <svg class="icon" viewBox="0 0 18 18" aria-label="Email"><circle cx="9" cy="9" r="9" fill="var(--icon-grey)"/><text x="9" y="13" text-anchor="middle" font-size="12" font-weight="700" fill="var(--brand-blue)" font-family="Arial, sans-serif">@</text></svg>
        henrique@verticenorte.example.pt
      </li>
      <li>
        <svg class="icon" viewBox="0 0 18 18" aria-label="Website"><circle cx="9" cy="9" r="9" fill="var(--icon-grey)"/><circle cx="9" cy="9" r="5" fill="none" stroke="var(--brand-blue)" stroke-width="1.3"/><ellipse cx="9" cy="9" rx="2.2" ry="5" fill="none" stroke="var(--brand-blue)" stroke-width="1.1"/><line x1="4" y1="9" x2="14" y2="9" stroke="var(--brand-blue)" stroke-width="1.1"/></svg>
        www.verticenorte.example.pt
      </li>
    </ul>
    <address class="contact__address">
      R. das Oliveiras, 71 - 2º<br>
      4100-218 Porto
    </address>
  </div>
</section>

<section class="card card--back" aria-label="Business card back">
  <div class="brand">
    <span class="brand__dot"></span>
    <div class="brand__name">Vertice Norte</div>
  </div>
</section>

</body>
</html>
```